2020 Camp Thornbrake Golf Tournament

We are looking for someone to design our 2020 Golf Tournament brochure that we will mail out to participants. I have uploaded a document that gives details along with last year's document so that you can have a point of reference.

The flyer will need to be 8.5 x 11, portrait style on one side and landscape on the other side. All the information is included in the document that has been provided.

Target Market(s)

Golfers and hole sponsors

Industry/Entity Type

Recreation

Colors

Designer to choose colors to be used in the design.

Requirements
Must have
• Provided information on the document.
Nice to have
• Cool design
Should not have
• Cartoon art

```html
<!DOCTYPE html>
<html lang="en">
<head>
<meta charset="utf-8">
<title>Camp Thornbrake Benefit Golf Tournament</title>
<link rel="stylesheet" href="https://fonts.googleapis.com/css2?family=Montserrat:wght@400;700;800&family=Oswald:wght@600&display=swap">
<style>
  :root {
    --page-bg: #67676a;
    --green-deep: #a1c43a;
    --green-mid: #b3d35c;
    --green-pale: #d8e48f;
    --green-corner: #b9d978;
    --fairway-light: #9ccc4f;
    --fairway-dark: #4f7a2c;
    --foliage: #3d5f26;
    --footer-bg: #e4e9b0;
    --footer-line: #c9da7a;
    --ink: #2c3a27;
    --ink-soft: #3b4536;
    --white: #ffffff;
  }
  * { margin: 0; padding: 0; box-sizing: border-box; }
  html, body {
    width: 1200px; height: 1200px; overflow: hidden;
    background: var(--page-bg);
  }
  .flyer {
    position: absolute; left: 238px; top: 132px;
    width: 723px; height: 936px;
    overflow: hidden; background: var(--fairway-light);
  }
  .flyer__photo {
    position: absolute; left: 0; top: 0; width: 723px; height: 872px;
    background: linear-gradient(180deg, var(--foliage) 0%, #5a8232 45%, #6f9f38 62%, var(--fairway-light) 78%, #8fc244 100%);
  }
  .flyer__waves { position: absolute; left: 0; top: 0; width: 723px; height: 936px; }
  .flyer__title-disc {
    position: absolute; left: -38px; top: 525px;
    width: 304px; height: 304px; border-radius: 50%;
    background: rgba(175, 212, 86, 0.55);
  }
  .flyer__title {
    position: absolute; left: 74px; top: 610px;
    font-family: "Montserrat", sans-serif; font-weight: 800;
    font-size: 35px; line-height: 43px; letter-spacing: 2.5px;
    color: var(--ink);
  }
  .brand {
    position: absolute; left: 87px; top: 48px;
    width: 208px; height: 208px; border-radius: 50%;
    background: var(--white);
    display: flex; align-items: center; justify-content: center;
  }
  .brand__name {
    font-family: "Oswald", sans-serif; font-weight: 600;
    font-size: 27px; line-height: 32px; text-align: center;
    color: var(--ink); text-transform: uppercase;
  }
  .flyer__footer {
    position: absolute; left: 0; top: 872px; width: 723px; height: 64px;
    background: var(--footer-bg); border-top: 4px solid var(--footer-line);
    font-family: "Montserrat", sans-serif; font-weight: 400;
    font-size: 12.5px; line-height: 16px; letter-spacing: 1.1px;
    color: var(--ink-soft); text-align: center;
    padding-top: 13px;
  }
  .flyer__footer strong { font-weight: 700; color: var(--ink); }
</style>
</head>
<body>
  <main class="flyer">
    <div class="flyer__photo" role="img" aria-label="Photo of a golfer in an orange shirt swinging a driver on a sunny fairway with green shrubs behind"></div>

    <svg class="flyer__waves" viewBox="0 0 904 1170" preserveAspectRatio="none" aria-hidden="true">
      <path d="M0 0 H904 V555 C850 480 760 440 620 415 C430 382 230 352 0 285 Z" fill="var(--green-pale)"/>
      <path d="M0 0 H904 V520 C840 450 740 410 600 390 C420 366 220 330 0 255 Z" fill="var(--green-mid)"/>
      <path d="M0 0 H904 V395 C800 330 650 300 480 310 C300 320 150 290 0 230 Z" fill="var(--green-deep)"/>
      <path d="M0 0 H60 C55 60 100 120 180 160 C120 170 60 190 0 225 Z" fill="var(--green-corner)"/>
      <path d="M180 0 H904 V70 C760 20 600 30 480 80 C380 120 260 90 180 0 Z" fill="#acd046" opacity="0.8"/>
    </svg>

    <div class="brand">
      <span class="brand__name">Camp<br>Thornbrake</span>
    </div>

    <div class="flyer__title-disc"></div>
    <h1 class="flyer__title">Benefit Golf<br>Tournament</h1>

    <footer class="flyer__footer">
      For more information call <strong>501-555-0148</strong> or email <strong>info@campthornbrake.org</strong>.<br>
      This form is also available on our website, campthornbrake.org.
    </footer>
  </main>
</body>
</html>
```